Business Card for Hollin Ledger - A cannabis publication for executives.

I'd like some business cards for Hollin Ledger. The logo is done (great job!) and I need a card design I will use with PELT. I made it a short project to allow time for printing before an event. These will be standard sized cards (final artwork size 3.66" x 2.16" at 300dpi) with a final card size of 3.5" x 2.0". (See PELT.example if you need more info.) I might try rounded corners but am not sure yet. I think the design will work okay with rounded.

Hollin Ledger will be a bi-weekly publication for the cannabis industry. It is targeted to investors and industry executives, not consumers or pot smokers. So our market is more B2B. However I am open to creativity and making the card something people remark on.

My contact for card:

Dara Venholm
Founder/CEO
dara@hollinledger.example

2746 Marrow Lane
Boston MA 02391
(617)555-0193

Target Market(s)

Executives, Industry people and investors in the Cannabis sector.

Contact Information for Business Card

PELT does do double sided and the second side can be the same or different images. Only one side is required but use of the second side would be a bonus.

Font styles to use
Serif
Sans Serif
Decorative

Colors

Designer to choose colors to be used in the design.

Requirements
Must have
• Logo, contact info
Nice to have
• Style and design to make the card stand out in a crowd.

```html
<!DOCTYPE html>
<html lang="en">
<head>
<meta charset="utf-8">
<title>Hollin Ledger – Business Card</title>
<link rel="stylesheet" href="https://fonts.googleapis.com/css2?family=Philosopher:wght@400;700&family=Open+Sans:wght@400;600&display=swap">
<style>
  :root {
    --page-bg: #e4e5e7;
    --card-white: #ffffff;
    --brand-green: #7cb233;
    --brand-green-dark: #64a01f;
    --brand-green-light: #9acd3c;
    --brand-blue: #1d6db5;
    --ink: #4a4a4a;
    --faint: #f1f5ec;
  }
  * { box-sizing: border-box; margin: 0; padding: 0; }
  html, body {
    width: 1200px; height: 1200px; overflow: hidden;
    background: var(--page-bg);
  }
  .canvas {
    position: relative; width: 1200px; height: 1200px;
  }
  .card {
    position: absolute; left: 180px; width: 840px; height: 480px;
    box-shadow: 0 6px 22px rgba(0,0,0,0.12);
    overflow: hidden;
  }
  /* Front */
  .card-front { top: 90px; background: var(--card-white); }
  .front-decoration {
    position: absolute; left: 70px; top: 70px; width: 300px; height: 300px;
    border-radius: 50%; background: var(--faint);
  }
  .front-logo {
    position: absolute; left: 420px; top: 78px;
    display: flex; align-items: center; gap: 18px;
  }
  .logo-square {
    width: 58px; height: 58px; background: var(--brand-green);
  }
  .logo-name {
    font-family: "Philosopher", sans-serif; font-weight: 700;
    font-size: 52px; color: var(--brand-blue); line-height: 1;
  }
  .name-band {
    position: absolute; left: 440px; right: 0; top: 210px; height: 58px;
    background: var(--brand-green);
    display: flex; align-items: center; padding-left: 22px; gap: 14px;
    color: #fff;
  }
  .person-name {
    font-family: "Philosopher", sans-serif; font-weight: 700; font-size: 30px;
  }
  .band-divider { width: 2px; height: 30px; background: rgba(255,255,255,0.8); }
  .person-title {
    font-family: "Open Sans", sans-serif; font-size: 18px;
  }
  .contact-list {
    position: absolute; left: 440px; top: 294px; list-style: none;
    font-family: "Open Sans", sans-serif; font-size: 19px; color: var(--ink);
    line-height: 1.45;
  }
  .contact-list li { display: flex; align-items: flex-start; gap: 10px; }
  .contact-list li + li { margin-top: 4px; }
  .contact-icon { width: 16px; height: 16px; margin-top: 6px; flex: none; fill: var(--brand-blue); }
  /* Back */
  .card-back {
    top: 630px;
    background: linear-gradient(135deg, var(--brand-green-dark) 0%, var(--brand-green) 50%, var(--brand-green-light) 100%);
    display: flex; align-items: center; justify-content: center;
  }
  .back-name {
    font-family: "Philosopher", sans-serif; font-weight: 700;
    font-size: 76px; color: #ffffff;
  }
</style>
</head>
<body>
<main class="canvas">
  <section class="card card-front" aria-label="Card front">
    <div class="front-decoration" aria-hidden="true"></div>
    <div class="front-logo">
      <div class="logo-square" aria-hidden="true"></div>
      <span class="logo-name">Hollin Ledger</span>
    </div>
    <div class="name-band">
      <span class="person-name">Dara Venholm</span>
      <span class="band-divider" aria-hidden="true"></span>
      <span class="person-title">Founder/CEO</span>
    </div>
    <ul class="contact-list">
      <li>
        <svg class="contact-icon" viewBox="0 0 16 16" aria-hidden="true"><path d="M2 6c0-2 2-3 6-3s6 1 6 3v1h-3V5.5H5V7H2zM4 8h8l1.5 5h-11z"/></svg>
        <span>(617)555-0193</span>
      </li>
      <li>
        <svg class="contact-icon" viewBox="0 0 16 16" aria-hidden="true"><path d="M1 3h14v10H1z M1 3l7 5 7-5" /></svg>
        <span>dara@hollinledger.example</span>
      </li>
      <li>
        <svg class="contact-icon" viewBox="0 0 16 16" aria-hidden="true"><path d="M8 0a5 5 0 0 1 5 5c0 4-5 11-5 11S3 9 3 5a5 5 0 0 1 5-5zm0 3a2 2 0 1 0 0 4 2 2 0 0 0 0-4z"/></svg>
        <span>2746 Marrow Lane<br>Boston MA 02391</span>
      </li>
    </ul>
  </section>

  <section class="card card-back" aria-label="Card back">
    <span class="back-name">Hollin Ledger</span>
  </section>
</main>
</body>
</html>
```